harvest Ahead Book Cover Design for real estate investment book

I am looking for a Book Cover design for my new book. I would like designs for a hardcover, softcover and Lumora book.

The book deals with real estate and mortgage investments. Looking for a clean, bright simple design. Want to cover to be White with big RED letters. See "Leading from Wonder" book for an example ... see attached.

Target Market(s)

Affluent people with money looking for investment solutions.

Industry/Entity Type

Financial Service

Font styles to use
Serif

Requirements
Must have
• Bright clean design that will be appealing to affluent people.
• Title: harvest AHEAD
• Subtitle: The quiet path to thriving through property holdings
• subsubtitle: Secrets Your Fund Manager Keeps Quiet About...
• Author: Ned Garroway
• My Picture on the inside cover or on the back cover
• Book Description, Author description
Nice to have
• Focus on the Front cover look and feel first. Then we can look at the inside flaps and back cover. I will need to send you text. This is for the full cover. Front. Back. Spine. Inside flaps fro hardcover.

```html
<!DOCTYPE html>
<html lang="en">
<head>
<meta charset="utf-8">
<title>Harvest Ahead — Front Cover</title>
<link rel="stylesheet" href="https://fonts.googleapis.com/css2?family=Sancreek&family=Libre+Baskerville:wght@400;700&family=Open+Sans:wght@700;800&display=swap">
<style>
  :root {
    --backdrop: #acd9d3;
    --cover-white: #ffffff;
    --title-red: #d9060f;
    --shadow: rgba(30, 70, 65, 0.28);
  }
  html, body {
    margin: 0;
    padding: 0;
    width: 1200px;
    height: 789px;
    overflow: hidden;
    background: var(--backdrop);
  }
  .stage {
    position: relative;
    width: 1200px;
    height: 789px;
  }
  .front-cover {
    position: absolute;
    left: 380px;
    top: 74px;
    width: 440px;
    height: 640px;
    background: var(--cover-white);
    box-shadow: 0 18px 40px var(--shadow);
  }
  .front-cover svg {
    display: block;
    width: 440px;
    height: 640px;
  }
  .subtitle {
    font-family: "Libre Baskerville", Georgia, serif;
    fill: var(--title-red);
  }
  .subtitle--lead { font-size: 15px; font-weight: 400; }
  .subtitle--main { font-size: 22px; font-weight: 700; }
  .title {
    font-family: "Sancreek", "Rye", serif;
    fill: var(--title-red);
  }
  .tagline {
    font-family: "Libre Baskerville", Georgia, serif;
    font-size: 11px;
    font-weight: 700;
    fill: var(--title-red);
  }
  .author {
    font-family: "Open Sans", Arial, sans-serif;
    font-size: 19px;
    font-weight: 800;
    fill: var(--title-red);
  }
</style>
</head>
<body>
<main class="stage">
  <article class="front-cover" aria-label="Front cover of Harvest Ahead by Ned Garroway">
    <svg viewBox="0 0 440 640" xmlns="http://www.w3.org/2000/svg">
      <text class="subtitle subtitle--lead" x="30" y="46" textLength="380" lengthAdjust="spacingAndGlyphs">THE QUIET PATH TO THRIVING</text>
      <text class="subtitle subtitle--main" x="30" y="76" textLength="380" lengthAdjust="spacingAndGlyphs">THROUGH PROPERTY HOLDINGS</text>

      <text class="title" x="24" y="330" font-size="230" textLength="392" lengthAdjust="spacingAndGlyphs">HARVEST</text>
      <text class="title" x="178" y="600" font-size="240" textLength="238" lengthAdjust="spacingAndGlyphs">AHEAD</text>

      <text class="tagline" x="26" y="378" textLength="142" lengthAdjust="spacingAndGlyphs">SECRETS YOUR FUND MANAGER</text>
      <text class="tagline" x="26" y="393" textLength="118" lengthAdjust="spacingAndGlyphs">KEEPS QUIET ABOUT...</text>
      <text class="author" x="26" y="420" textLength="140" lengthAdjust="spacingAndGlyphs">NED GARROWAY</text>
    </svg>
  </article>
</main>
</body>
</html>
```